Business Cards for an 'affordable luxury' inner city home builder in Calgary.

We need a business card design that emulates the progressive, innovative, culture of our company and the modern style of our homes. Use our website www.velmarcrest-ab.com as a reference for the product we build.

Our company builds homes in the inner city space of Calgary, Alberta. We build affordable luxury.

Target Market(s)

Young professional Families

Contact Information for Business Card

Try to maintain consistency with the logo font and the card font.

Requirements
Must have
• The details must include: Name, education, title, phone number, website and email (Address is not as important)
• The design must be uniques (like our logo), elegant, sophisticated and modern.

```html
<!DOCTYPE html>
<html lang="en">
<head>
<meta charset="utf-8">
<title>Velmarcrest Homes Ltd — Business Cards</title>
<link href="https://fonts.googleapis.com/css2?family=Montserrat:wght@500&family=PT+Sans+Narrow:wght@400;700&display=swap" rel="stylesheet">
<style>
  :root {
    --backdrop: #e7e4e1;
    --card: #1c1d1f;
    --ink: #f4f4f4;
    --ink-soft: #d9d9d9;
    --foil: #6a6c70;
    --rule: #c9c9c9;
  }
  * { margin: 0; padding: 0; box-sizing: border-box; }
  html, body { width: 1200px; height: 864px; overflow: hidden; }
  body {
    background: var(--backdrop);
    position: relative;
    font-family: "PT Sans Narrow", "Arial Narrow", sans-serif;
  }
  .card {
    position: absolute;
    width: 540px;
    height: 308px;
    background: var(--card);
    box-shadow: 0 10px 30px rgba(0,0,0,.25);
    color: var(--ink);
  }
  .card--front { left: 40px; top: 110px; }
  .card--back  { left: 620px; top: 446px; }

  .wordmark {
    display: flex;
    align-items: center;
    gap: 14px;
    font-family: "Montserrat", sans-serif;
    font-weight: 500;
    text-transform: uppercase;
    line-height: 1.0;
  }
  .wordmark__square {
    width: 34px; height: 34px;
    border: 2px solid currentColor;
    flex: none;
  }
  .card--front .wordmark {
    position: absolute; left: 70px; top: 92px;
    color: var(--foil);
    font-size: 26px;
    letter-spacing: 1px;
  }
  .card--front .wordmark__square { width: 48px; height: 48px; }
  .front-url {
    position: absolute; left: 70px; bottom: 58px;
    font-size: 16px;
    letter-spacing: 6px;
    color: var(--ink-soft);
  }

  .card--back .wordmark {
    position: absolute; left: 34px; top: 112px;
    font-size: 17px;
    letter-spacing: .5px;
  }
  .divider {
    position: absolute; left: 282px; top: 56px;
    width: 1px; height: 196px;
    background: var(--rule);
  }
  .details {
    position: absolute; left: 304px; top: 58px;
    width: 220px;
  }
  .details__name {
    font-weight: 700;
    font-size: 22px;
    margin-bottom: 4px;
  }
  .details__role {
    font-size: 14px;
    line-height: 1.2;
    color: var(--ink-soft);
  }
  .details__address {
    font-size: 15px;
    margin-top: 12px;
  }
  .contact { list-style: none; margin-top: 2px; }
  .contact li {
    display: flex; align-items: center; gap: 6px;
    font-size: 15px;
    line-height: 1.3;
  }
  .contact svg { width: 12px; height: 12px; flex: none; fill: var(--ink); }
</style>
</head>
<body>

  <section class="card card--front" aria-label="Card front">
    <div class="wordmark">
      <span class="wordmark__square"></span>
      <span>Velmarcrest<br>Homes Ltd</span>
    </div>
    <p class="front-url">www.velmarcrest-ab.com</p>
  </section>

  <section class="card card--back" aria-label="Card back">
    <div class="wordmark">
      <span class="wordmark__square"></span>
      <span>Velmarcrest<br>Homes Ltd</span>
    </div>
    <div class="divider"></div>
    <div class="details">
      <h1 class="details__name">Tavinder</h1>
      <p class="details__role">Co-Founder<br>Business Development / Strategy<br>Professional Engineer (P.ENG)<br>Masters of Business Administration (MBA)</p>
      <p class="details__address">418 17 Ave NW, Calgary, AB</p>
      <ul class="contact">
        <li>
          <svg viewBox="0 0 12 12" aria-hidden="true"><path d="M2.5 1l2 2.2-1 1.3c.7 1.5 1.6 2.4 3 3l1.3-1 2.2 2-1.2 2C5.5 10.3 1.7 6.5 1 2.2z"/></svg>
          403-555-0148
        </li>
        <li>
          <svg viewBox="0 0 12 12" aria-hidden="true"><path d="M1 2.5h10v7H1z M1.5 3l4.5 3.5L10.5 3" stroke="#1c1d1f" stroke-width=".8"/></svg>
          projects@velmarcrest-ab.com
        </li>
        <li>
          <svg viewBox="0 0 12 12" aria-hidden="true"><circle cx="6" cy="6" r="5"/><path d="M1 6h10M6 1c2 2 2 8 0 10M6 1c-2 2-2 8 0 10" stroke="#1c1d1f" stroke-width=".7" fill="none"/></svg>
          www.velmarcrest-ab.com
        </li>
      </ul>
    </div>
  </section>

</body>
</html>
```